Kestrel Photography Business Card

I need a business card designed for a photography business based in Perth, Western Australia called Kestrel Photography.

We specialise in wedding, event photography and portrait photography.

The business card must borrow the style of the attached logo.

The hex codes for the colours in the logo are:
#ED1D85 - Pink
#89C23E - Green
#37282F - Black

The name on the card will be:
Name: Toviran
Phone: 0417395268
Website: www.kestrelphotography.com.au
Facebook: kestrelphotography

I am open and happy to accept creative concepts.

I’d like some space at the back for writing notes and appointment details.

```html
<!DOCTYPE html>
<html lang="en">
<head>
<meta charset="utf-8">
<title>Kestrel Photography Business Card</title>
<link rel="stylesheet" href="https://fonts.googleapis.com/css2?family=Arimo:wght@400;700&display=swap">
<style>
  :root {
    --card-pink: #d95f89;
    --band-dark: #3a2d33;
    --brand-pink: #ed1d85;
    --brand-green: #89c23e;
    --brand-black: #37282f;
    --contact-pink: #e46fa0;
    --paper: #ffffff;
    --sheet: #ffffff;
  }
  * { box-sizing: border-box; margin: 0; padding: 0; }
  html, body { width: 1200px; height: 338px; overflow: hidden; background: var(--sheet); }
  body { font-family: "Arimo", Arial, sans-serif; position: relative; }

  .card {
    position: absolute;
    top: 0;
    width: 576px;
    height: 336px;
    background: var(--card-pink);
    overflow: hidden;
  }
  .card--front { left: 0; border: 1px solid #b8577b; }
  .card--back { left: 624px; }

  .holder-name {
    position: absolute;
    left: 32px;
    top: 62px;
    color: var(--paper);
    font-weight: 700;
    font-size: 33px;
  }

  .brand-mark {
    position: absolute;
    border-radius: 50%;
    background: radial-gradient(circle, #c95580 0%, #e0689a 55%, #e986ad 100%);
  }
  .brand-mark--front { left: 366px; top: 26px; width: 64px; height: 64px; }
  .brand-mark--faint { left: 32px; top: 144px; width: 92px; height: 92px; opacity: .45; }
  .brand-mark--back { left: 228px; top: 22px; width: 104px; height: 104px; }

  .brand-name {
    position: absolute;
    color: var(--brand-black);
    font-weight: 400;
    text-transform: uppercase;
    white-space: nowrap;
  }
  .brand-name--front { left: 262px; top: 108px; font-size: 10px; letter-spacing: 5.4px; }
  .brand-name--back { left: 0; width: 576px; text-align: center; top: 172px; font-size: 16px; letter-spacing: 13px; padding-left: 13px; }

  .contact-band {
    position: absolute;
    left: 0; bottom: 0;
    width: 100%;
    height: 82px;
    background: var(--band-dark);
    display: flex;
    flex-direction: column;
    align-items: center;
    justify-content: center;
    gap: 5px;
    font-weight: 700;
    font-size: 15px;
  }
  .contact-line { display: flex; align-items: center; gap: 8px; }
  .contact-line svg { width: 18px; height: 18px; flex: none; }
  .contact-line--phone { color: var(--contact-pink); }
  .contact-line--web { color: var(--brand-green); }
  .contact-line--social { color: var(--contact-pink); }

  .writing-area {
    position: absolute;
    left: 0; bottom: 0;
    width: 100%;
    height: 72px;
    background: var(--paper);
  }
  .writing-row {
    height: 33px;
    border-bottom: 3px solid var(--card-pink);
    display: flex;
    align-items: center;
    padding-left: 52px;
    font-size: 15px;
    font-weight: 700;
    color: #1e1a1c;
  }
</style>
</head>
<body>

<section class="card card--front">
  <h1 class="holder-name">Toviran</h1>
  <div class="brand-mark brand-mark--front" role="img" aria-label="Kestrel Photography emblem"></div>
  <p class="brand-name brand-name--front">Kestrel Photography</p>
  <div class="brand-mark brand-mark--faint" role="img" aria-label="Faint Kestrel Photography emblem"></div>

  <div class="contact-band">
    <div class="contact-line contact-line--phone">
      <svg viewBox="0 0 18 18" aria-hidden="true">
        <rect x="1" y="1" width="16" height="16" rx="3" fill="#4a8fd0"/>
        <path d="M5 6.5c0-1 .8-1.5 4-1.5s4 .5 4 1.5v1h-2.2v-1H7.2v1H5z" fill="#fff"/>
        <rect x="5.5" y="9" width="7" height="5" rx="1" fill="#fff"/>
      </svg>
      <span>0417395268</span>
    </div>
    <div class="contact-line contact-line--web">
      <svg viewBox="0 0 18 18" aria-hidden="true">
        <circle cx="9" cy="9" r="7.5" fill="#6fa8dc" stroke="#fff" stroke-width="1"/>
        <ellipse cx="9" cy="9" rx="3" ry="7.5" fill="none" stroke="#fff" stroke-width="1"/>
        <line x1="1.5" y1="9" x2="16.5" y2="9" stroke="#fff" stroke-width="1"/>
      </svg>
      <span>www.kestrelphotography.com.au</span>
    </div>
    <div class="contact-line contact-line--social">
      <svg viewBox="0 0 18 18" aria-hidden="true"><rect x="1" y="1" width="16" height="16" rx="2" fill="#4a6aa8"/></svg>
      <span>kestrelphotography</span>
    </div>
  </div>
</section>

<section class="card card--back">
  <div class="brand-mark brand-mark--back" role="img" aria-label="Kestrel Photography emblem"></div>
  <p class="brand-name brand-name--back">Kestrel Photography</p>

  <div class="writing-area">
    <div class="writing-row">Notes :</div>
    <div class="writing-row">Appointment :</div>
  </div>
</section>

</body>
</html>
```